Flyer Design

Create a flyer using the logo theme. Single page for to be sent out on email. Attached is an image of the layout, below is the text. A5 and a4 versions.

Simplifying the MAZE

This short workshop is designed as a refresher for those surgeons who have attended a full Lund-MAZE training course, and wish to gain an update on the latest thinking with regards to the surgical treatment of Atrial Fibrillation.
We will start with an overview of the disease burden, talk to the foundation clinical evidence available, and cover the various lesion sets used by surgeons – with a view to simplifying the procedure. The workshop will also explain the technology used, how to treat the Left Atrial Appendage, the best ways to work with your EP colleagues, and involve a short hands-on session to familiarize you with the tools available to perform the Lund-MAZE procedure.

Faculty
{{image}}
Mr. Declan Harlow
Cardiothoracic Surgeon

Mr Harlows training was completed at the Brenhill Clinic, Rochester, Minnesota, between June 1995 and July 1997 followed by an advanced fellowship with Professor Ferris K Lomond at the Ashgrove General Hospital. Additional expertise required visits to Belgium, Italy, England and the United States. Mr Harlow now proctors internationally in order to share his knowledge and further improvement in all areas of minimal access and open cardiac and thoracic surgery.
Further overseas experience at the Ashgrove General Hospital in Canada culminated in the award of Clinical Fellowship in Cardiovascular Surgery in December 1997.

Mr Harlow has contributed to many publications and is referee for Journal articles in very highly regarded professional journals. He performs both Cardiac surgery procedures and thoracic procedures at Westmere Private Hospital and Dunmore Hospital, Melbourne. Mr Harlow has performed in excess of 200 open Maze procedures and 35 via a Thoracoscopic approach.

Venue - TBA
Time : 5pm - 7.30pm, followed by dinner and case presentations

```html
<!DOCTYPE html>
<html lang="en">
<head>
<meta charset="utf-8">
<title>Simplifying the MAZE – Workshop Flyer</title>
<link rel="stylesheet" href="https://fonts.googleapis.com/css2?family=Lato:wght@400;700;900&family=Roboto:wght@500;700&display=swap">
<style>
  :root {
    --page-bg: #e8e5e0;
    --brand-blue: #1a6aa0;
    --brand-blue-deep: #134f7f;
    --brand-navy: #0f3d63;
    --brand-sky: #1d86c6;
    --brand-orange: #f28a1e;
    --paper: #ffffff;
    --text-light: #ffffff;
  }
  html, body {
    margin: 0;
    width: 1127px;
    height: 1200px;
    overflow: hidden;
    background: var(--page-bg);
    font-family: "Lato", sans-serif;
  }
  .flyer {
    position: absolute;
    left: 154px;
    top: 20px;
    width: 819px;
    height: 1160px;
    background: linear-gradient(160deg, var(--brand-blue) 0%, var(--brand-blue-deep) 100%);
    box-shadow: 0 4px 14px rgba(0,0,0,0.35);
    overflow: hidden;
  }
  .flyer-shapes { position: absolute; inset: 0; }
  .heart-art {
    position: absolute;
    left: 381px;
    top: 660px;
    width: 300px;
    height: 500px;
    border-radius: 48% 52% 40% 60% / 45% 45% 55% 55%;
    background: radial-gradient(ellipse at 50% 50%, rgba(140,190,228,0.28) 0%, rgba(120,175,220,0.12) 55%, rgba(120,175,220,0) 75%);
  }
  .brand-name {
    position: absolute;
    left: 540px;
    top: 44px;
    margin: 0;
    font-family: "Lato", sans-serif;
    font-weight: 700;
    font-size: 48px;
    line-height: 1;
    color: var(--brand-sky);
    letter-spacing: -0.5px;
  }
  .event-title {
    position: absolute;
    left: 84px;
    top: 139px;
    width: 269px;
    height: 52px;
    margin: 0;
    background: var(--brand-orange);
    color: var(--text-light);
    font-weight: 700;
    font-size: 25px;
    line-height: 52px;
    text-align: center;
  }
  .event-copy {
    position: absolute;
    left: 84px;
    top: 217px;
    width: 441px;
    color: var(--text-light);
    font-size: 14.8px;
    line-height: 21.6px;
    text-align: justify;
  }
  .event-copy p { margin: 0 0 21.6px; }
  .event-copy p.gap-lg { margin-bottom: 30px; }
  .event-copy p.tight { margin-bottom: 0; }
  .faculty-label {
    position: absolute;
    left: 575px;
    top: 237px;
    width: 171px;
    height: 39px;
    margin: 0;
    padding-left: 12px;
    box-sizing: border-box;
    background: var(--brand-sky);
    color: var(--text-light);
    font-weight: 700;
    font-size: 23px;
    line-height: 39px;
  }
  .faculty-photo {
    position: absolute;
    left: 577px;
    top: 294px;
    width: 169px;
    height: 206px;
    background: linear-gradient(180deg, #b9c9b3 0%, #8c8f8a 45%, #2a2d33 100%);
  }
  .faculty-name {
    position: absolute;
    left: 577px;
    top: 518px;
    margin: 0;
    color: var(--text-light);
    font-weight: 700;
    font-size: 22px;
  }
  .faculty-role {
    position: absolute;
    left: 577px;
    top: 556px;
    margin: 0;
    color: var(--text-light);
    font-weight: 700;
    font-size: 17px;
    line-height: 21px;
  }
  .event-details {
    position: absolute;
    left: 46px;
    top: 1030px;
  }
  .detail-row { display: flex; align-items: flex-start; margin-bottom: 14px; }
  .detail-icon { width: 26px; height: 28px; margin-right: 22px; flex-shrink: 0; }
  .detail-main {
    margin: 0;
    font-family: "Roboto", sans-serif;
    font-weight: 700;
    font-size: 21px;
    color: var(--brand-blue);
    line-height: 26px;
  }
  .detail-sub {
    margin: 2px 0 0;
    font-weight: 700;
    font-size: 13.5px;
    color: #333a40;
  }
</style>
</head>
<body>
<main class="flyer">
  <svg class="flyer-shapes" width="819" height="1160" viewBox="0 0 819 1160" aria-hidden="true">
    <path d="M298,0 C342,84 488,178 819,208 L819,0 Z" fill="var(--brand-navy)"/>
    <path d="M316,0 C360,78 502,164 819,190 L819,0 Z" fill="var(--brand-orange)"/>
    <path d="M334,0 C380,70 520,150 819,174 L819,0 Z" fill="var(--paper)"/>
    <path d="M360,0 C404,60 540,132 819,158" fill="none" stroke="var(--brand-orange)" stroke-width="1.2"/>
    <path d="M0,930 C230,934 470,1030 600,1160 L0,1160 Z" fill="var(--brand-navy)"/>
    <path d="M0,946 C215,950 445,1045 555,1160 L0,1160 Z" fill="var(--brand-orange)"/>
    <path d="M0,962 C200,968 420,1060 522,1160 L0,1160 Z" fill="var(--paper)"/>
    <path d="M0,978 C190,985 400,1070 490,1160" fill="none" stroke="var(--brand-orange)" stroke-width="1.2"/>
  </svg>

  <div class="heart-art" role="img" aria-label="Faint anatomical heart illustration in pale blue"></div>

  <p class="brand-name">Veloria</p>

  <h1 class="event-title">Simplifying the MAZE</h1>

  <section class="event-copy">
    <p>This short workshop is designed as a refresher for those surgeons who have attended a full Lund-MAZE training course, and wish to gain an update on the latest thinking with regards to the surgical treatment of Atrial Fibrillation.</p>
    <p class="gap-lg">We will start with an overview of the disease burden, talk to the foundation clinical evidence available, and cover the various lesion sets used by surgeons – with a view to simplifying the procedure. The workshop will also explain the technology used, how to treat the Left Atrial Appendage, the best ways to work with your EP colleagues, and involve a short hands-on session to familiarize you with the tools available to perform the Lund-MAZE procedure.</p>
    <p class="tight">Mr Harlows training was completed at the Brenhill Clinic, Rochester, Minnesota, between June 1995 and July 1997 followed by an advanced fellowship with Professor Ferris K Lomond at the Ashgrove General Hospital. Additional expertise required visits to Belgium, Italy, England and the United States. Mr Harlow now proctors internationally in order to share his knowledge and further improvement in all areas of minimal access and open cardiac and thoracic surgery.</p>
    <p>Further overseas experience at the Ashgrove General Hospital in Canada culminated in the award of Clinical Fellowship in Cardiovascular Surgery in December 1997.</p>
    <p>Mr Harlow has contributed to many publications and is referee for Journal articles in very highly regarded professional journals. He performs both Cardiac surgery procedures and thoracic procedures at Westmere Private Hospital and Dunmore Hospital, Melbourne. Mr Harlow has performed in excess of 200 open Maze procedures and 35 via a Thoracoscopic approach.</p>
  </section>

  <h2 class="faculty-label">Faculty</h2>
  <div class="faculty-photo" role="img" aria-label="Portrait photo of the faculty surgeon"></div>
  <p class="faculty-name">Mr. Declan Harlow</p>
  <p class="faculty-role">Cardiothoracic<br>Surgeon</p>

  <section class="event-details">
    <div class="detail-row">
      <svg class="detail-icon" viewBox="0 0 26 28" aria-hidden="true">
        <path d="M13,1 C7,1 3,5.5 3,11 C3,18 13,27 13,27 C13,27 23,18 23,11 C23,5.5 19,1 13,1 Z" fill="var(--brand-orange)"/>
        <circle cx="13" cy="11" r="4" fill="var(--paper)"/>
      </svg>
      <p class="detail-main">Venue - TBA</p>
    </div>
    <div class="detail-row">
      <svg class="detail-icon" viewBox="0 0 26 28" aria-hidden="true">
        <circle cx="13" cy="14" r="10.5" fill="none" stroke="var(--brand-orange)" stroke-width="2.6"/>
        <path d="M13,8 V14 H18" fill="none" stroke="var(--brand-orange)" stroke-width="2.6" stroke-linecap="round"/>
      </svg>
      <div>
        <p class="detail-main">Time : 5pm - 7.30pm,</p>
        <p class="detail-sub">followed by dinner and case presentations</p>
      </div>
    </div>
  </section>
</main>
</body>
</html>
```